Präsentationsvorlagen für Hausarztpraxis
Zielgruppe
Neue Hausarztpraxis, Zielgruppe junge Patienten
Es ist gedacht für eine Präsentation die im WArtezimmer auf dem T V läuft... daher seitenaufbau variieren.
Aufgabenstellung
es sollte zum Logo passen.. modern sein, verschiedene Seiten ( nicht jede Seite sollte gleich aussehen) ich sollte es mit Pages bearbeiten können. In der Präsentation soll die Praxis vorgstellt werden, mit den Sprechzeiten, Website, dem Team, Dem leistungsspektrum, erweiterte Dinge wie NEU Ultraschalluntersuchungen der Schilddrüse, Bauch und Gefäße, auch eine Seite zu den neuen Hyaloronsäure Fillern... ich werden heute Abend noch mehr schreiben was mit untergebracht werden sollte
Farbe bitte wie das Logo halten...

```html
<!DOCTYPE html>
<html lang="de">
<head>
<meta charset="utf-8">
<title>Hausarztpraxis Dr. med. Lena Aurich – Wartezimmer-Präsentation</title>
<link rel="stylesheet" href="https://fonts.googleapis.com/css2?family=Open+Sans:wght@700&family=Source+Sans+3:wght@300;400&display=swap">
<style>
  :root {
    --berry: #b7364b;
    --coral: #e94f60;
    --ink: #555555;
    --white: #ffffff;
    --paper: #ffffff;
  }
  html, body {
    margin: 0;
    padding: 0;
    width: 1200px;
    height: 3000px;
    overflow: hidden;
    background: var(--paper);
  }
  .canvas {
    position: relative;
    width: 1200px;
    height: 3000px;
    overflow: hidden;
  }
  .stage {
    position: absolute;
    left: 85px;
    top: 0;
    width: 1030px;
    height: 3000px;
  }
  .box { position: absolute; }
  .berry { background: var(--berry); }
  .coral { background: var(--coral); }

  .headline {
    position: absolute;
    margin: 0;
    font-family: "Open Sans", Arial, sans-serif;
    font-weight: 700;
    color: var(--berry);
    line-height: 1.22;
  }
  .body-text {
    position: absolute;
    margin: 0;
    font-family: "Source Sans 3", Arial, sans-serif;
    font-weight: 300;
    font-size: 21px;
    line-height: 26px;
    color: var(--ink);
  }

  /* Praxis wordmark */
  .wordmark {
    position: absolute;
    display: flex;
    flex-direction: column;
    align-items: center;
    gap: 6px;
  }
  .wordmark-dot {
    border-radius: 50%;
    background: var(--berry);
  }
  .wordmark-name {
    font-family: "Source Sans 3", Arial, sans-serif;
    font-weight: 400;
    color: var(--berry);
    white-space: nowrap;
    letter-spacing: 0.04em;
  }
  .wordmark.large .wordmark-dot { width: 58px; height: 58px; }
  .wordmark.large .wordmark-name { font-size: 22px; }
  .wordmark.small .wordmark-dot { width: 34px; height: 34px; }
  .wordmark.small .wordmark-name { font-size: 13px; }

  /* Slide 1 – Willkommen */
  .welcome-title {
    left: 117px; top: 380px;
    font-size: 58px;
    color: var(--white);
    line-height: 1.2;
  }
  .photo-town {
    left: 513px; top: 0; width: 464px; height: 580px;
    background: linear-gradient(180deg, #cfe0ec 0%, #e6edf2 35%, #6e6466 60%, #8b8888 100%);
  }

  /* Slide 2 – Sprechstunden */
  .frame-line { position: absolute; background: var(--berry); }
  .photo-phone {
    left: 93px; top: 640px; width: 423px; height: 578px;
    background: linear-gradient(160deg, #dcdbd7 0%, #d3d2ce 100%);
  }

  /* Slide 3 – Leistungen */
  .photo-room {
    left: 167px; top: 1372px; width: 863px; height: 518px;
    background: linear-gradient(180deg, #e2e1de 0%, #ecebe8 55%, #c9b8a0 82%, #b9a68c 100%);
  }
  .services-text { color: var(--white); font-weight: 300; }

  /* Slide 4 – Team */
  .team-photo { position: absolute; top: 2190px; height: 290px; }
  .name-bar {
    position: absolute;
    top: 2447px; height: 58px; width: 233px;
    background: var(--coral);
    color: var(--white);
    font-family: "Source Sans 3", Arial, sans-serif;
    font-weight: 400;
    font-size: 28px;
    line-height: 58px;
    padding-left: 29px;
    box-sizing: border-box;
  }
</style>
</head>
<body>
<div class="canvas">
  <div class="stage">

    <!-- Slide 1: Willkommen -->
    <section class="slide slide-welcome">
      <div class="box berry" style="left:38px; top:0; width:475px; height:580px;"></div>
      <div class="box photo-town" role="img" aria-label="Foto: historische Fachwerkhäuser an einem gepflasterten Marktplatz"></div>
      <div class="box coral" style="left:463px; top:17px; width:100px; height:41px;"></div>
      <div class="box coral" style="left:711px; top:402px; width:319px; height:101px;"></div>
      <div class="wordmark large" style="left:600px; top:28px; width:290px;">
        <span class="wordmark-dot"></span>
        <span class="wordmark-name">Dr. med. Lena Aurich</span>
      </div>
      <h1 class="headline welcome-title">Herzlich<br>Willkommen!</h1>
    </section>

    <!-- Slide 2: Sprechstunden -->
    <section class="slide slide-hours">
      <div class="box photo-phone" role="img" aria-label="Foto: alter schwarzer Telefonhörer an einem Kabel vor hellgrauem Hintergrund"></div>
      <div class="frame-line" style="left:38px; top:640px; width:3px; height:531px;"></div>
      <div class="frame-line" style="left:38px; top:1168px; width:313px; height:3px;"></div>
      <div class="frame-line" style="left:452px; top:640px; width:3px; height:503px;"></div>
      <div class="box coral" style="left:351px; top:1143px; width:222px; height:41px;"></div>
      <div class="wordmark small" style="left:826px; top:664px; width:164px;">
        <span class="wordmark-dot"></span>
        <span class="wordmark-name">Dr. med. Lena Aurich</span>
      </div>
      <h2 class="headline" style="left:576px; top:752px; font-size:43px;">Unsere neuen<br>Sprechstunden</h2>
      <p class="body-text" style="left:573px; top:883px; width:420px;">
        Mo 8-11:30 sowie 14-17 Uhr<br>
        Die 8-13 Uhr / Mi 8-13 Uhr<br>
        Do 8-11:30 sowie 14-18 Uhr<br>
        Fr 8-11:30<br><br>
        Telefonisch erreichen Sie uns täglich von 8:30-11:oo Uhr sowie Montags und Donnerstags von 14:oo-16:oo Uhr.
      </p>
    </section>

    <!-- Slide 3: Leistungsspektrum -->
    <section class="slide slide-services">
      <div class="box photo-room" role="img" aria-label="Foto: heller Behandlungsraum mit Liege, Hocker, Uhr und Bild an der Wand"></div>
      <div class="wordmark small" style="left:826px; top:1366px; width:164px;">
        <span class="wordmark-dot"></span>
        <span class="wordmark-name">Dr. med. Lena Aurich</span>
      </div>
      <h2 class="headline" style="left:63px; top:1570px; font-size:44px;">Unser Leistungsspektrum</h2>
      <div class="box berry" style="left:0; top:1632px; width:561px; height:240px;"></div>
      <p class="body-text services-text" style="left:63px; top:1662px; width:485px;">
        Vollständige hausärztliche Versorgung / Gesundheitsvorsorge / Krebsvorsorge / EKG und Ergometrie / Sonographie Bauch, Schilddrüse, Gefäße / Langzeitblutdruckmessung / Lungenfunktionsprüfung / Laboruntersuchungen / Sämtliche Impfungen / Kleine operative Eingriffe &nbsp;/ Wundversorgung / Autogenes Training / Neuraltherapie
      </p>
    </section>

    <!-- Slide 4: Team -->
    <section class="slide slide-team">
      <div class="wordmark small" style="left:826px; top:2020px; width:164px;">
        <span class="wordmark-dot"></span>
        <span class="wordmark-name">Dr. med. Lena Aurich</span>
      </div>
      <h2 class="headline" style="left:112px; top:2096px; font-size:42px;">Das sind wir – unser Team</h2>
      <div class="team-photo" style="left:114px; width:233px; background:linear-gradient(180deg,#e9ecec 0%,#d8dcdc 100%);" role="img" aria-label="Teamfoto: Ärztin im weißen Kittel mit Stethoskop"></div>
      <div class="team-photo" style="left:418px; width:205px; background:linear-gradient(180deg,#e8e8e6 0%,#d9dad8 100%);" role="img" aria-label="Teamfoto: Ärztin mit Brille, Klemmbrett und Stethoskop"></div>
      <div class="team-photo" style="left:694px; width:222px; background:linear-gradient(180deg,#7f9a4e 0%,#a4b673 55%,#e9e9e4 100%);" role="img" aria-label="Teamfoto: Ärztin im weißen Kittel vor grünen Bäumen"></div>
      <div class="name-bar" style="left:93px;">Name</div>
      <div class="name-bar" style="left:394px;">Name</div>
      <div class="name-bar" style="left:674px;">Name</div>
    </section>

  </div>
</div>
</body>
</html>
```